Sydney law firm, Prestwicks Solicitors, needs a flyer design!

We need a flyer design for our law firm which has been operating in Sydney for over 35 years. We want to send the flyer out to potential clients and also to existing clients to let them know the range of services that we provide. Our corporate colours are white, red and black and we would like these incorporated somewhat. The final design should be clean, modern and professional.

We would like the design to fit a double sided flyer approx. 210mm high x 100mm wide.

Industry/Entity Type

Law Firm

Font styles to use
Serif
Sans Serif

Colors
eb2026
ffffff

Requirements
Must have
• Details needed on the flyer are:
• Prestwicks Solicitors
• 3/82 Carradine Street, Liverpool, NSW 2170
• (02) 9418 3562
• www.prestwickssolicitors-example.com.au
• info@prestwickssolicitors-example.com.au
• Our areas of practice include:
• Property Law
• Conveyancing
• Leases
• Criminal Law
• Family Law
• Litigation and Dispute Resolution
• Company Law
• Wills and Estates
• Powers of Attorney and Guardianship
Should not have
• a picture of scales or a picture of a gavel

```html
<!DOCTYPE html>
<html lang="en">
<head>
<meta charset="utf-8">
<title>Prestwicks Solicitors – Flyer</title>
<link rel="stylesheet" href="https://fonts.googleapis.com/css2?family=Open+Sans:wght@400;600;700&display=swap">
<style>
  :root {
    --red: #c0281f;
    --black: #121212;
    --white: #ffffff;
    --ink: #1a1a1a;
    --grey-light: #f2f2f2;
    --grey-mid: #d6d6d6;
    --photo-dark: #3a3a3a;
    --photo-light: #cfcfcf;
  }
  * { margin: 0; padding: 0; box-sizing: border-box; }
  html, body { width: 1200px; height: 2517px; overflow: hidden; background: var(--white); }
  .flyer {
    position: relative; width: 1200px; height: 2517px; overflow: hidden;
    font-family: "Open Sans", Arial, sans-serif; color: var(--ink); background: var(--white);
  }
  .hero-bg {
    position: absolute; left: 0; top: 0; width: 1200px; height: 666px;
    background: linear-gradient(180deg, var(--grey-light), var(--grey-mid));
  }
  .phone-band {
    position: absolute; left: 0; top: 666px; width: 1200px; height: 155px; background: var(--red);
  }
  .hero-frame { position: absolute; left: 0; top: 0; width: 1200px; height: 821px; }
  .phone {
    position: absolute; right: 42px; top: 736px; display: flex; align-items: center; gap: 10px;
    color: var(--white); font-weight: 700; font-size: 58px; line-height: 1; letter-spacing: 1px;
  }
  .phone svg { width: 52px; height: 52px; }
  .brand {
    position: absolute; left: 0; top: 848px; width: 1200px; text-align: center;
    color: var(--black); font-weight: 700; line-height: 1;
  }
  .brand-name { font-size: 120px; }
  .brand-sub { font-size: 46px; margin-top: 22px; }
  .intro-lead { position: absolute; right: 42px; top: 1108px; font-weight: 700; font-size: 42px; }
  .intro {
    position: absolute; left: 38px; top: 1167px; width: 1140px;
    font-size: 41px; line-height: 58.6px; white-space: nowrap;
  }
  .about {
    position: absolute; left: 52px; top: 1585px; width: 1130px;
    font-size: 39px; line-height: 58.6px; white-space: nowrap;
  }
  .services { position: absolute; left: 0; top: 0; width: 1200px; }
  .service {
    position: absolute; display: flex; align-items: center; justify-content: center;
    color: var(--white); font-weight: 700; font-size: 43px; letter-spacing: 1.5px; white-space: nowrap;
  }
  .service.red { background: var(--red); }
  .service.black { background: var(--black); }
  .contact-bar {
    position: absolute; left: 0; top: 2349px; width: 1200px; height: 168px; background: var(--black);
    color: var(--white); display: flex; align-items: center;
  }
  .address { width: 500px; text-align: center; font-size: 37px; line-height: 46px; }
  .online { font-weight: 700; font-size: 28.5px; line-height: 44px; }
</style>
</head>
<body>
<div class="flyer">
  <div class="hero-bg"></div>
  <div class="phone-band"></div>

  <svg class="hero-frame" viewBox="0 0 1200 821">
    <defs>
      <linearGradient id="photoTone" x1="0" y1="0" x2="1" y2="0.4">
        <stop offset="0" stop-color="#3a3a3a"/>
        <stop offset="0.55" stop-color="#6a6a6a"/>
        <stop offset="1" stop-color="#cfcfcf"/>
      </linearGradient>
    </defs>
    <polygon points="200,70 1110,40 1115,705 345,765" fill="#000"/>
    <polygon role="img" aria-label="Black and white photograph of two people shaking hands" points="225,30 1138,0 1138,665 360,742" fill="url(#photoTone)"/>
  </svg>

  <div class="phone">
    <svg viewBox="0 0 52 52" aria-hidden="true">
      <circle cx="26" cy="26" r="23" fill="none" stroke="#ffffff" stroke-width="4"/>
      <path d="M19 14c3 0 4 6 2 8l-2 2c1 4 4 7 8 8l2-2c2-2 8-1 8 2 0 3-3 6-7 5-9-2-15-8-17-17-1-4 3-6 6-6z" fill="#ffffff"/>
    </svg>
    <span>(02) 9418 3562</span>
  </div>

  <div class="brand">
    <div class="brand-name">PRESTWICKS</div>
    <div class="brand-sub">SOLICITORS</div>
  </div>

  <p class="intro-lead">At Prestwicks Solicitors,</p>
  <p class="intro">Our clients benefit from our extensive knowledge of<br>the law, vast network of professional and legal<br>advisers as well as our unmatched client service<br>experience. We understand the complex nature of<br>the law and legal transactions and strive to simplify<br>the process for our clients.</p>

  <p class="about">Prestwicks is a Private Law Firm that has been servicing the<br>Sydney area for over 35 years. With a dedicated,<br>professional and friendly team we pride ourselves on<br>delivering an exceptional legal service to our clients.<br>We provide legal service in the areas of:</p>

  <div class="services">
    <div class="service red"   style="left:0;top:1895px;width:362px;height:95px">Property Law</div>
    <div class="service black" style="left:362px;top:1890px;width:396px;height:95px">Conveyancing</div>
    <div class="service red"   style="left:758px;top:1895px;width:442px;height:95px">Wills and Estates</div>

    <div class="service black" style="left:0;top:2008px;width:412px;height:96px">Criminal Law</div>
    <div class="service red"   style="left:412px;top:2003px;width:411px;height:96px">Family Law</div>
    <div class="service black" style="left:823px;top:2010px;width:377px;height:96px">company Law</div>

    <div class="service red"   style="left:0;top:2121px;width:270px;height:92px">Leases</div>
    <div class="service black" style="left:270px;top:2121px;width:930px;height:92px">Litigation and Dispute Resolution</div>

    <div class="service red"   style="left:0;top:2232px;width:1200px;height:93px">Powers of Attorney and Guardianship</div>
  </div>

  <div class="contact-bar">
    <div class="address">3/82 Carradine Street,<br>Liverpool, NSW 2170</div>
    <div class="online">www.prestwickssolicitors-example.com.au<br>info@prestwickssolicitors-example.com.au</div>
  </div>
</div>
</body>
</html>
```